Query A Legal Mentor

We need banner ad design for a new company that supplies supplemental study materials for law students. All content on the site is completely free and we assist law students with supplemental materials for daily course work and for preparing for final exams. The site provides free: Q&A - all answers provided by law professors, Audio Lectures on the most important law school topics, Outline Overviews, Charts and Notes of difficult and confusing law school topics, mini essays with answers for exam preparation.
Updates

ads need to be in the following sizes: 728x90, 160x600, 300x250, 468x60, 120x240

Reason: the ad target market are 'professional students' so it cannot look childish in design. The design must be professional looking.

Target Market(s)

Law Students .. review the QueryALegalMentor.example site

Industry/Entity Type

School

Requirements
Must have
• The word 'Free' must be very prominent throughout the ads
Nice to have
• Try to include 'all of the free items' that are included that the user receives once the register for free for the site. Also the ads may include animation so that each free item the user receives may be able to stand out better.

```html
<!DOCTYPE html>
<html lang="en">
<head>
<meta charset="utf-8">
<title>Query A Legal Mentor – Banner Set</title>
<link rel="stylesheet" href="https://fonts.googleapis.com/css2?family=Encode+Sans+Condensed:wght@600;700&family=Arimo:wght@700&display=swap">
<style>
  :root {
    --brand-blue: #1a80c4;
    --bar-blue: #0b84c3;
    --button-blue: #1285c8;
    --bullet-green: #1fe01f;
    --panel-white: #ffffff;
    --stage: #eceef1;
    --photo-light: #dfe6ee;
    --photo-mid: #b9c6d3;
    --photo-dark: #3a4452;
  }
  * { box-sizing: border-box; margin: 0; padding: 0; }
  html, body { width: 1200px; height: 900px; overflow: hidden; }
  body { background: var(--stage); position: relative; font-family: "Arimo", Arial, sans-serif; }

  .banner { position: absolute; background: var(--panel-white); overflow: hidden; box-shadow: 0 2px 8px rgba(0,0,0,.15); }
  .banner > * { position: absolute; }

  .headline {
    font-family: "Encode Sans Condensed", "Arial Narrow", sans-serif;
    font-weight: 700; color: var(--brand-blue); text-align: center;
    text-transform: uppercase; white-space: nowrap; z-index: 2;
  }

  .benefits { list-style: none; color: var(--brand-blue); font-weight: 700; font-size: 17px; z-index: 2; }
  .benefits li { display: flex; align-items: center; height: 24px; white-space: nowrap; }
  .benefits li::before {
    content: ""; width: 12px; height: 12px; border-radius: 50%;
    background: var(--bullet-green); margin-right: 7px; flex: none;
  }

  .enroll-button {
    background: var(--button-blue); color: #fff; border-radius: 9px;
    font-weight: 700; font-size: 21px; display: flex; align-items: center; justify-content: center;
  }

  .brand-name {
    font-family: "Arimo", Arial, sans-serif; font-weight: 700; color: #fff;
    white-space: nowrap; display: flex; align-items: center; justify-content: center;
  }

  .photo {
    background: linear-gradient(160deg, var(--photo-light) 0%, var(--photo-mid) 55%, var(--photo-dark) 100%);
  }

  .footer-bar {
    background: var(--bar-blue); display: flex; align-items: center; justify-content: space-between;
    padding: 0 12px;
  }
  .footer-bar .cta { color: #fff; font-weight: 700; font-size: 22px; display: flex; align-items: center; gap: 8px; }

  /* Leaderboard 728x90 */
  .leaderboard { left: 239px; top: 42px; width: 853px; height: 105px; }
  .leaderboard .headline { left: 10px; top: 12px; width: 196px; font-size: 21px; line-height: 27px; }
  .leaderboard .benefits { left: 226px; top: 4px; }
  .leaderboard .brand-tab { left: 440px; top: 0; width: 193px; height: 40px; background: var(--bar-blue); font-size: 16px; }
  .leaderboard .enroll-button { left: 463px; top: 54px; width: 149px; height: 46px; }
  .leaderboard .photo { left: 643px; top: 0; width: 210px; height: 105px; }

  /* Medium rectangle 300x250 */
  .rectangle { left: 404px; top: 250px; width: 394px; height: 328px; }
  .rectangle .headline { left: 0; top: 6px; width: 394px; font-size: 22px; line-height: 28px; }
  .rectangle .photo { left: 186px; top: 64px; width: 208px; height: 219px; }
  .rectangle .benefits { left: 6px; top: 106px; }
  .rectangle .footer-bar { left: 0; top: 283px; width: 394px; height: 45px; }
  .rectangle .brand-name { font-size: 18px; }

  /* Skyscraper 160x600 */
  .skyscraper { left: 905px; top: 183px; width: 187px; height: 702px; }
  .skyscraper .headline { left: 0; top: 18px; width: 187px; font-size: 21px; line-height: 27px; }
  .skyscraper .benefits { left: 6px; top: 126px; }
  .skyscraper .enroll-button { left: 18px; top: 294px; width: 156px; height: 51px; }
  .skyscraper .photo { left: 0; top: 360px; width: 187px; height: 298px; }
  .skyscraper .footer-bar { left: 0; top: 658px; width: 187px; height: 44px; justify-content: center; padding: 0 4px; }
  .skyscraper .brand-name { font-size: 14px; }
</style>
</head>
<body>

  <section class="banner leaderboard" aria-label="728 by 90 banner">
    <h2 class="headline">Free Law School<br>Supplemental<br>Materials</h2>
    <ul class="benefits">
      <li>Q &amp; A</li>
      <li>Topic Videos</li>
      <li>Audio lectures</li>
      <li>Outline Overviews</li>
    </ul>
    <div class="brand-name brand-tab">Query A Legal Mentor</div>
    <div class="enroll-button">Enroll Now</div>
    <div class="photo" role="img" aria-label="Photo of two smiling law students in business attire"></div>
  </section>

  <section class="banner rectangle" aria-label="300 by 250 banner">
    <h2 class="headline">Free Law School Supplemental<br>Materials</h2>
    <div class="photo" role="img" aria-label="Photo of two smiling law students in business attire"></div>
    <ul class="benefits">
      <li>Q &amp; A</li>
      <li>Topic Videos</li>
      <li>Audio lectures</li>
      <li>Outline Overviews</li>
      <li>Charts and Notes</li>
      <li>Mini Essays</li>
    </ul>
    <div class="footer-bar">
      <span class="cta">Enroll Now
        <svg width="18" height="16" viewBox="0 0 18 16" aria-hidden="true"><path d="M2 2l6 6-6 6M9 2l6 6-6 6" fill="none" stroke="#fff" stroke-width="3"/></svg>
      </span>
      <span class="brand-name">Query A Legal Mentor</span>
    </div>
  </section>

  <section class="banner skyscraper" aria-label="160 by 600 banner">
    <h2 class="headline">Free Law School<br>Supplemental<br>Materials</h2>
    <ul class="benefits">
      <li>Q &amp; A</li>
      <li>Topic Videos</li>
      <li>Audio lectures</li>
      <li>Outline Overviews</li>
      <li>Charts and Notes</li>
      <li>Mini Essays</li>
    </ul>
    <div class="enroll-button">Enroll Now</div>
    <div class="photo" role="img" aria-label="Photo of two smiling law students in business attire"></div>
    <div class="footer-bar"><span class="brand-name">Query A Legal Mentor</span></div>
  </section>

</body>
</html>
```